Design refresh of existing HR Application

QuillStaff is an HR & Payroll processing software, already in use by thousands of people. It is a feature packed, enterprise-grade software that is also simple and user friendly. Visit us at https://quillstaff.example

Seeking a refresh of the app design/UI.

Key objectives are to make it "sleeker", more professional and polished, whist still retaining functionality. Not intended to be a massive overhaul, but more of reorganization and improvements on design elements.

You may login to our demo account to see the app live.
https://app.quillstaff.example/login
User: demo@quillstaff.example
Password: Zip20

Target Market(s)

HR Managers, business administrators/owners and employees.

Industry/Entity Type

Business Software

Number of Pages Required

4 page

Font styles to use
Other font styles liked:
• Lato

Colors
0255a3
3377b5
00a990
33b8a4
f37122
faa54b

Requirements
Must have
• Must retain the current functionality on each page.
Nice to have
• Fine to suggest changes to colors, font sizes, card designs, moving sections around and any other design element changes.

```html
<!DOCTYPE html>
<html lang="en">
<head>
<meta charset="utf-8">
<title>QuillStaff – HR App Refresh</title>
<link href="https://fonts.googleapis.com/css2?family=Lato:wght@400;700;900&display=swap" rel="stylesheet">
<style>
:root{
  --stage:#179c80;
  --brand-blue:#2b63ac;
  --link-blue:#0255a3;
  --header:#0e2b2a;
  --sidebar:#252525;
  --sidebar-line:#333;
  --page:#eeeeee;
  --card:#ffffff;
  --teal:#00a990;
  --teal-light:#33b8a4;
  --orange:#f37122;
  --orange-light:#faa54b;
  --red:#e8202a;
  --green:#22a06b;
  --ink:#222;
  --muted:#666;
  --rule:#e3e3e3;
  --grid-a:#e6e6e6;
  --grid-b:#d7d7d7;
  --grid-block:#a8a8a8;
}
*{box-sizing:border-box;margin:0;padding:0}
html,body{width:1123px;height:1200px;overflow:hidden}
body{background:var(--stage);font-family:'Lato',sans-serif;color:var(--ink);position:relative}
.screen{position:absolute;width:837px;transform-origin:0 0;transform:scale(.6035);background:var(--page);overflow:hidden}
.abs{position:absolute}
/* sidebar */
.sidebar{position:absolute;left:0;top:0;bottom:0;width:180px;background:var(--sidebar)}
.brand{height:56px;background:var(--brand-blue);display:flex;align-items:center;padding-left:28px;gap:10px}
.brand-dot{width:22px;height:22px;border-radius:50%;border:3px solid #fff}
.brand-name{color:#fff;font-size:25px;font-weight:400;letter-spacing:.3px}
.nav-item{height:37px;border-bottom:1px solid var(--sidebar-line);display:flex;align-items:center;padding-left:33px;gap:12px;color:#fff;font-size:7.5px;font-weight:700;letter-spacing:.3px}
.nav-item.active{background:#f7993a}
.nav-icon{width:7px;height:7px;background:#fff;border-radius:1px}
.powered{position:absolute;left:33px;bottom:38px;color:#bbb;font-size:7.5px}
.powered b{color:var(--orange-light);font-weight:400;font-size:10px;margin-left:4px}
.legal{position:absolute;left:33px;bottom:18px;color:#777;font-size:7px}
/* header */
.topbar{position:absolute;left:180px;right:0;top:0;height:56px;background:var(--header);color:#fff}
.lang{position:absolute;right:208px;top:23px;font-size:8px;font-weight:700}
.help{position:absolute;right:177px;top:23px;width:8px;height:8px;border-radius:50%;background:#fff}
.avatar{border-radius:50%;background:linear-gradient(135deg,#c9a58c,#8a6a55)}
.user{position:absolute;right:40px;top:15px}
.user .avatar{position:absolute;left:-34px;top:0;width:29px;height:29px}
.user strong{display:block;font-size:11px;font-weight:700}
.user small{font-size:7px;font-weight:700}
/* tiles */
.tile{position:absolute;width:137px;height:51px;color:#fff;padding:8px 10px}
.tile .num{position:absolute;right:10px;top:6px;font-size:22px;font-weight:300}
.tile .lbl{position:absolute;left:12px;bottom:6px;font-size:8px;font-weight:700;letter-spacing:.2px}
.tile svg{position:absolute;left:12px;top:9px}
.t1{background:#21a58e}.t2{background:var(--teal-light)}.t3{background:#ec5b24}.t4{background:#f7993a}
.h{position:absolute;font-size:10.5px;font-weight:700;color:#222;letter-spacing:.2px}
.star{position:absolute;font-size:8px;font-weight:700;color:var(--link-blue)}
.card{position:absolute;background:var(--card);box-shadow:0 1px 2px rgba(0,0,0,.08)}
.row{position:absolute;left:0;right:0;border-bottom:1px solid var(--rule);font-size:7.5px;display:flex;align-items:center}
.pill{display:inline-block;color:#fff;font-size:7px;padding:3px 10px;border-radius:2px}
.pill.round{border-radius:10px}
.bg-orange{background:var(--orange)}.bg-red{background:var(--red)}.bg-teal{background:var(--teal-light)}.bg-blue{background:var(--brand-blue)}
.select{position:absolute;height:21px;background:#fff;border:1px solid #ccc;font-size:7px;padding:6px 7px;color:#333}
.select::after{content:"⬍";position:absolute;right:6px;top:5px;font-size:7px}
.select.plain::after{content:""}
/* payroll table */
.ptable{position:absolute;left:199px;top:237px;width:596px;background:#fff}
.prow{display:grid;grid-template-columns:86px 67px 71px 80px 66px 56px 49px 53px 68px;border-bottom:1px solid var(--rule);height:38.8px;align-items:center;font-size:7px}
.prow>div{padding-left:10px}
.prow.head{background:#f5f5f5;font-weight:700;font-size:7px;height:40px;color:#333}
.prow .nm{color:var(--link-blue);line-height:1.2}
.prow .nm b{display:block;color:#222}
.or{color:var(--orange)}.bl{color:var(--link-blue)}.rd{color:var(--red)}
.cash{display:inline-block;width:11px;height:7px;border:1.5px solid var(--green);border-radius:1px}
.status{display:inline-block;font-size:6.5px;color:#fff;background:var(--orange);padding:3px 8px}
.status.ok{background:var(--green)}
.pager{position:absolute;top:948px;left:409px;display:flex;gap:6px}
.pager span{width:20px;height:20px;font-size:8px;display:flex;align-items:center;justify-content:center;background:#fff}
.pager .dark{background:#222;color:#fff}.pager .on{background:#f7993a;color:#fff}
/* weekly */
.tabs span{position:absolute;font-size:8px;font-weight:700}
.dayhead{position:absolute;top:212px;width:59px;height:32px;background:#fff;text-align:center;font-size:8px;color:var(--link-blue);padding-top:5px;line-height:1.25}
.dayhead small{font-size:7px;font-weight:700}
.shift{position:absolute;width:48px;height:14px;font-size:6px;color:#fff;display:flex;align-items:center;justify-content:center}
.shift.we{background:#444}.shift.wd{background:var(--orange)}
.emp{position:absolute;left:0;height:30px;width:837px;border-bottom:1px solid #ddd}
.emp .avatar{position:absolute;left:12px;top:7px;width:16px;height:16px}
.emp .nm{position:absolute;left:36px;top:4px;color:var(--teal);font-size:8.5px;font-weight:700}
.emp .sub{position:absolute;left:36px;top:16px;font-size:6.5px;color:#333}
.emp .hrs{position:absolute;left:150px;top:11px;font-size:8px;width:10px;text-align:center}
/* profile modal */
.modal{position:absolute;left:13px;top:0;width:810px;height:823px;background:#fff}
.mhead{position:absolute;left:0;right:0;top:0;height:70px;background:var(--header);color:#fff}
.mtabs span{position:absolute;top:86px;font-size:8px;font-weight:700}
.hist-row{position:absolute;left:0;right:0;height:34px;border-bottom:1px solid var(--rule);font-size:7.5px}
.hist-row span{position:absolute;top:13px}
.xbtn{position:absolute;width:22px;height:22px;border-radius:50%;background:var(--red);color:#fff;font-size:10px;font-weight:700;display:flex;align-items:center;justify-content:center}
</style>
</head>
<body>

<!-- DASHBOARD -->
<section class="screen" style="left:47px;top:39px;height:974px">
  <aside class="sidebar">
    <div class="brand"><span class="brand-dot"></span><span class="brand-name">QuillStaff</span></div>
    <div class="nav-item active"><i class="nav-icon"></i>DASHBOARD</div>
    <div class="nav-item"><i class="nav-icon"></i>EMPLOYEES</div>
    <div class="nav-item"><i class="nav-icon"></i>CALENDAR</div>
    <div class="nav-item"><i class="nav-icon"></i>EXPENSES</div>
    <div class="nav-item"><i class="nav-icon"></i>PAYROLL</div>
    <div class="nav-item"><i class="nav-icon"></i>LOANS</div>
    <div class="nav-item"><i class="nav-icon"></i>PERFORMANCE</div>
    <div class="nav-item"><i class="nav-icon"></i>ENGAGEMENT</div>
    <div class="nav-item"><i class="nav-icon"></i>REPORTS</div>
    <div class="nav-item"><i class="nav-icon"></i>SETTINGS</div>
    <div class="powered">Powered by: <b>QuillStaff</b></div>
    <div class="legal">Terms | Privacy</div>
  </aside>
  <header class="topbar">
    <span class="lang">English ⌄</span><span class="help"></span>
    <div class="user"><span class="avatar" role="img" aria-label="Admin profile photo"></span><strong>Admin, Demo</strong><small>HR Administrator ⌄</small></div>
  </header>

  <h2 class="h" style="left:199px;top:72px">QUICK LINKS</h2>
  <div class="tile t1" style="left:199px;top:97px"><svg width="20" height="17" viewBox="0 0 20 17" fill="none" stroke="#fff" stroke-width="1.3"><rect x="1" y="2" width="18" height="14"/><path d="M1 6h18M5 0v4M15 0v4M5 10h2M9 10h2M13 10h2"/></svg><span class="num">12</span><span class="lbl">EVENT AMENDMENTS</span></div>
  <div class="tile t2" style="left:352px;top:97px"><svg width="18" height="18" viewBox="0 0 18 18" fill="none" stroke="#fff" stroke-width="1.3"><rect x="2" y="1" width="13" height="16"/><path d="M5 5h7M5 9h7M5 13h5"/></svg><span class="num">2</span><span class="lbl">LEAVE REQUESTS</span></div>
  <div class="tile t3" style="left:505px;top:97px"><svg width="20" height="18" viewBox="0 0 20 18" fill="none" stroke="#fff" stroke-width="1.3"><rect x="1" y="3" width="14" height="14"/><circle cx="14" cy="7" r="5"/></svg><span class="num">7</span><span class="lbl">EVENT REQUESTS</span></div>
  <div class="tile t4" style="left:658px;top:97px"><svg width="20" height="18" viewBox="0 0 20 18" fill="none" stroke="#fff" stroke-width="1.3"><rect x="1" y="1" width="14" height="16"/><path d="M4 5h8M4 9h5"/><circle cx="15" cy="13" r="4"/></svg><span class="num">1</span><span class="lbl">PAYROLLS PENDING</span></div>

  <h2 class="h" style="left:199px;top:167px">TODAY'S EVENT</h2>
  <h2 class="h" style="left:350px;top:167px">MY SCHEDULE</h2>
  <h2 class="h" style="left:659px;top:167px">MY TIME OFF</h2>

  <div class="card" style="left:199px;top:191px;width:137px;height:127px;text-align:center">
    <div class="abs" style="left:33px;top:13px;width:70px;height:70px;border-radius:50%;border:2px solid #ddd;border-bottom-color:var(--orange);font-size:34px;font-weight:700;line-height:66px">0</div>
    <div class="abs" style="left:0;right:0;top:92px;font-size:8px;font-weight:700;line-height:1.3">NO SCHEDULED EVENTS<br>TODAY</div>
  </div>

  <div class="card" style="left:350px;top:191px;width:300px;height:127px">
    <div class="abs" style="left:12px;top:16px;font-size:7px;line-height:1.35"><b class="bl">Thu, May28</b><br>10:00 Work (Project A) 12:00 Branch A</div>
    <div class="abs" style="left:12px;top:54px;font-size:7px;line-height:1.35"><b class="bl">Thu, May28</b><br>10:00 Work (Project A) 12:00 Branch A</div>
    <div class="abs" style="left:12px;top:92px;font-size:7px;line-height:1.35"><b class="bl">Thu, May28</b><br>10:00 Work (Project A) 12:00 Branch A</div>
    <div class="abs" style="left:164px;top:0;width:1px;height:127px;background:var(--rule)"></div>
    <div class="abs" style="left:178px;top:10px;width:112px;font-size:8.5px;color:var(--teal);text-align:center">‹ &nbsp;&nbsp; MAY 2020 &nbsp;&nbsp; ›</div>
    <svg class="abs" style="left:172px;top:30px" width="122" height="92" viewBox="0 0 122 92" font-family="Lato,sans-serif" font-size="6.5" fill="#555" text-anchor="middle">
      <g fill="#333"><circle cx="8" cy="5" r="4.5" fill="#777"/><circle cx="24" cy="5" r="4.5"/><circle cx="40" cy="5" r="4.5"/><circle cx="56" cy="5" r="4.5"/><circle cx="72" cy="5" r="4.5"/><circle cx="88" cy="5" r="4.5"/><circle cx="104" cy="5" r="4.5"/></g>
      <g fill="#fff" font-size="5"><text x="8" y="7">S</text><text x="24" y="7">M</text><text x="40" y="7">T</text><text x="56" y="7">W</text><text x="72" y="7">T</text><text x="88" y="7">F</text><text x="104" y="7">S</text></g>
      <text x="88" y="23">1</text><text x="104" y="23">2</text>
      <text x="8" y="39">3</text><text x="24" y="39">4</text><text x="40" y="39">5</text><text x="56" y="39">6</text><text x="72" y="39">7</text><text x="88" y="39">8</text><text x="104" y="39">9</text>
      <text x="8" y="55">10</text><text x="24" y="55">11</text><text x="40" y="55">12</text><text x="56" y="55">13</text><text x="72" y="55">14</text><text x="88" y="55">15</text><text x="104" y="55">16</text>
      <text x="8" y="71">17</text><text x="24" y="71">18</text><text x="40" y="71">19</text><text x="56" y="71">20</text><text x="72" y="71">21</text><text x="88" y="71">22</text><text x="104" y="71">23</text>
      <text x="8" y="87">24</text><text x="24" y="87">25</text><text x="40" y="87">26</text><text x="56" y="87">27</text><text x="72" y="87">28</text><text x="88" y="87">29</text><text x="104" y="87">30</text>
    </svg>
  </div>

  <div class="card" style="left:659px;top:191px;width:136px;height:127px">
    <svg class="abs" style="left:10px;top:14px" width="28" height="28" viewBox="0 0 28 28"><rect x="2" y="4" width="24" height="22" rx="2" fill="#e8f3fb" stroke="#2b63ac"/><rect x="2" y="4" width="24" height="6" fill="#e8202a"/><path d="M9 18l4 4 7-8" stroke="#e8202a" stroke-width="2" fill="none"/></svg>
    <div class="abs" style="left:48px;top:13px;font-size:8px;font-weight:700">ANNUAL LEAVE</div>
    <div class="abs" style="left:48px;top:22px;font-size:24px;font-weight:700;color:var(--link-blue)">6</div>
    <div class="abs" style="left:68px;top:33px;font-size:8px;font-weight:700">LEFT</div>
    <div class="abs" style="left:0;right:0;top:57px;height:1px;background:var(--rule)"></div>
    <svg class="abs" style="left:12px;top:68px" width="26" height="26" viewBox="0 0 26 26" fill="none" stroke="#2b63ac" stroke-width="2"><path d="M5 2v8a6 6 0 0 0 12 0V2M11 16v3a5 5 0 0 0 10 0v-4"/><circle cx="21" cy="13" r="2"/></svg>
    <div class="abs" style="left:48px;top:68px;font-size:8px;font-weight:700">SICK DAYS</div>
    <div class="abs" style="left:48px;top:77px;font-size:24px;font-weight:700;color:var(--link-blue)">1</div>
    <div class="abs" style="left:68px;top:88px;font-size:8px;font-weight:700">TAKEN</div>
    <div class="abs" style="left:0;right:0;bottom:0;height:23px;background:var(--orange);color:#fff;font-size:9px;font-weight:700;text-align:center;line-height:23px">REQUEST</div>
  </div>

  <h2 class="h" style="left:199px;top:337px">TARDY TODAY</h2>
  <span class="star" style="left:410px;top:338px">★ &nbsp;VIEW STARTED</span>
  <h2 class="h" style="left:505px;top:337px">ANNOUNCEMENTS</h2>
  <span class="star" style="left:716px;top:338px">★ &nbsp;VIEW STARTED</span>

  <div class="card" style="left:199px;top:361px;width:289px;height:166px">
    <div class="row" style="top:8px;height:25px"><span class="avatar" role="img" aria-label="Employee photo" style="width:14px;height:14px;margin:0 12px 0 10px"></span><span style="width:132px">100, Employee</span><span style="width:103px">HR Administrator</span>8.0</div>
    <div class="row" style="top:33px;height:25px"><span class="avatar" role="img" aria-label="Employee photo" style="width:14px;height:14px;margin:0 12px 0 10px"></span><span style="width:132px">100, Employee</span><span style="width:103px">Factory Worker</span>8.0</div>
    <div class="row" style="top:58px;height:25px"><span class="avatar" role="img" aria-label="Employee photo" style="width:14px;height:14px;margin:0 12px 0 10px"></span><span style="width:132px">91, Employee</span><span style="width:103px">HR Administrator</span>8.0</div>
    <div class="row" style="top:83px;height:25px"><span class="avatar" role="img" aria-label="Employee photo" style="width:14px;height:14px;margin:0 12px 0 10px"></span><span style="width:132px">Employee, Demo</span><span style="width:103px">HR Manager</span>8.0</div>
    <div class="row" style="top:108px;height:25px"><span class="avatar" role="img" aria-label="Employee photo" style="width:14px;height:14px;margin:0 12px 0 10px"></span><span style="width:132px">70, Employee</span><span style="width:103px">Shipping Manager</span>7.0</div>
    <div class="row" style="top:133px;height:25px;border:0"><span class="avatar" role="img" aria-label="Employee photo" style="width:14px;height:14px;margin:0 12px 0 10px"></span><span style="width:132px">Manager, Demo</span><span style="width:103px">HR Manager</span>9.0</div>
  </div>

  <div class="card" style="left:505px;top:361px;width:290px;height:166px">
    <div class="row" style="top:8px;height:25px;padding-left:14px">Have a great Hari Lahir Pancasila on 2020-06-01!<span style="margin-left:auto;margin-right:12px;color:var(--link-blue)">›</span></div>
    <div class="row" style="top:33px;height:40px;padding-left:14px;line-height:1.8">Free Friday drinks are available in the pantry on every week until the<br>end of this year. Take the opportunity to get to know more people!</div>
  </div>

  <h2 class="h" style="left:199px;top:547px">EMPLOYEE UPDATES</h2>
  <span class="star" style="left:358px;top:548px">★ &nbsp;VIEW STARTED</span>
  <h2 class="h" style="left:453px;top:548px">WHO'S ON LEAVE TODAY</h2>
  <span class="star" style="left:580px;top:549px">⊤ &nbsp;FILTER</span>
  <span class="abs" style="left:634px;top:550px;font-size:6.5px;font-style:italic;color:#333"><span style="color:var(--teal)">Same Department</span> / Same Branch / Subordinates</span>

  <div class="card" style="left:199px;top:569px;width:239px;height:166px"><div class="abs" style="left:0;right:0;top:78px;text-align:center;font-size:8.5px">There are no Announcements</div></div>
  <div class="card" style="left:453px;top:569px;width:342px;height:166px">
    <div class="row" style="top:5px;height:32px"><span class="avatar" role="img" aria-label="Employee photo" style="width:14px;height:14px;margin:0 12px 0 10px"></span><span style="width:94px">34, Employee</span><span style="width:124px">HR Administrator</span><span class="pill round bg-orange" style="width:82px;text-align:center">Maternity Leave</span></div>
    <div class="row" style="top:37px;height:32px"><span class="avatar" role="img" aria-label="Employee photo" style="width:14px;height:14px;margin:0 12px 0 10px"></span><span style="width:94px">34, Employee</span><span style="width:124px">HR Administrator</span><span class="pill round bg-orange" style="width:82px;text-align:center">Maternity Leave</span></div>
  </div>

  <h2 class="h" style="left:199px;top:756px">NOTIFICATIONS</h2>
  <div class="card" style="left:199px;top:777px;width:596px;height:167px">
    <div class="row" style="top:8px;height:25px;padding-left:14px"><span style="width:20px;color:var(--link-blue)">▭</span><span style="width:376px">Sari, Melati has remotely checked in for Working on</span><span style="width:77px">20/05/2020</span>02:07</div>
    <div class="row" style="top:33px;height:25px;padding-left:14px"><span style="width:20px;color:var(--link-blue)">☂</span><span style="width:376px">Sari, Melati requests amendment on</span><span style="width:77px">15 Apr 2020</span>from 09:00 - 18:00.</div>
    <div class="row" style="top:58px;height:25px;padding-left:14px"><span style="width:20px;color:var(--link-blue)">■</span><span style="width:376px">Overtime request for Sari, Melati</span><span style="width:77px">18 May 2020</span>at 19:00 | 21:00 Branch A</div>
    <div class="row" style="top:83px;height:25px;padding-left:14px"><span style="width:20px;color:var(--link-blue)">▭</span><span style="width:376px">Sari, Melati requests Sick Leave on</span><span style="width:77px">19 May 2020</span></div>
    <div class="row" style="top:108px;height:25px;padding-left:14px"><span style="width:20px;color:var(--link-blue)">☂</span><span style="width:376px">Sari, Melati requests amendment on</span><span style="width:77px">30 Apr 2020</span>from 10:00 - 18:00</div>
    <div class="row" style="top:133px;height:25px;padding-left:14px;border:0"><span style="width:20px;color:var(--link-blue)">▭</span><span style="width:376px">Sari, Melati requests amendment on</span><span style="width:77px">15 Apr 2020</span>from 09:00 - 18:00.</div>
  </div>
</section>

<!-- PAYROLL -->
<section class="screen" style="left:578px;top:39px;height:990px">
  <aside class="sidebar">
    <div class="brand"><span class="brand-dot"></span><span class="brand-name">QuillStaff</span></div>
    <div class="nav-item"><i class="nav-icon"></i>DASHBOARD</div>
    <div class="nav-item"><i class="nav-icon"></i>EMPLOYEES</div>
    <div class="nav-item"><i class="nav-icon"></i>CALENDAR</div>
    <div class="nav-item"><i class="nav-icon"></i>EXPENSES</div>
    <div class="nav-item active"><i class="nav-icon"></i>PAYROLL</div>
    <div class="nav-item"><i class="nav-icon"></i>LOANS</div>
    <div class="nav-item"><i class="nav-icon"></i>PERFORMANCE</div>
    <div class="nav-item"><i class="nav-icon"></i>ENGAGEMENT</div>
    <div class="nav-item"><i class="nav-icon"></i>REPORTS</div>
    <div class="nav-item"><i class="nav-icon"></i>SETTINGS</div>
    <div class="powered">Powered by: <b>QuillStaff</b></div>
    <div class="legal">Terms | Privacy</div>
  </aside>
  <header class="topbar">
    <span class="lang">English ⌄</span><span class="help"></span>
    <div class="user"><span class="avatar" role="img" aria-label="Admin profile photo"></span><strong>Admin, Demo</strong><small>HR Administrator ⌄</small></div>
  </header>

  <div class="tile t1" style="left:199px;top:70px"><svg width="20" height="17" viewBox="0 0 20 17" fill="none" stroke="#fff" stroke-width="1.3"><rect x="1" y="2" width="18" height="14"/><path d="M1 6h18M5 0v4M15 0v4"/></svg><span class="num">12</span><span class="lbl">EVENT AMENDMENTS</span></div>
  <div class="tile t2" style="left:352px;top:70px"><svg width="18" height="18" viewBox="0 0 18 18" fill="none" stroke="#fff" stroke-width="1.3"><rect x="2" y="1" width="13" height="16"/><path d="M5 5h7M5 9h7M5 13h5"/></svg><span class="num">2</span><span class="lbl">LEAVE REQUESTS</span></div>
  <div class="tile t3" style="left:505px;top:70px"><svg width="20" height="18" viewBox="0 0 20 18" fill="none" stroke="#fff" stroke-width="1.3"><rect x="1" y="3" width="14" height="14"/><circle cx="14" cy="7" r="5"/></svg><span class="num">7</span><span class="lbl">EVENT REQUESTS</span></div>
  <div class="tile t4" style="left:658px;top:70px"><svg width="20" height="18" viewBox="0 0 20 18" fill="none" stroke="#fff" stroke-width="1.3"><rect x="1" y="1" width="14" height="16"/><circle cx="15" cy="13" r="4"/></svg><span class="num">1</span><span class="lbl">PAYROLLS PENDING</span></div>

  <div class="abs" style="left:180px;right:0;top:141px;height:46px;background:#fff;font-size:8px">
    <div class="abs" style="left:19px;top:14px">MONTHLY<br><b style="font-size:8.5px">01 May 2020 - 31 May 2020</b></div>
    <div class="abs" style="left:132px;top:6px;color:var(--link-blue);font-size:9.5px;font-weight:700;line-height:1.05">⟳<br>Change<br><span style="font-size:7px">Batch</span></div>
    <div class="abs" style="left:184px;top:8px;width:1px;height:30px;background:var(--rule)"></div>
    <div class="abs" style="left:206px;top:14px">TOTAL PAYABLE<br><b style="font-weight:400;font-size:8.5px">1,995,673,256.94</b></div>
    <div class="abs" style="left:294px;top:14px">TOTAL PAYSLIPS<br><span style="font-size:8.5px">1,095</span></div>
    <div class="abs" style="left:368px;top:8px;width:1px;height:30px;background:var(--rule)"></div>
    <div class="abs" style="left:378px;top:18px;color:var(--link-blue);font-size:10px;font-weight:700">▦ Calculator <span style="color:#aaa">🗑</span></div>
    <div class="abs" style="left:468px;top:8px;width:1px;height:30px;background:var(--rule)"></div>
    <div class="abs" style="left:479px;top:14px">BATCH STATUS<br><span style="font-size:8.5px">Pending</span></div>
    <div class="abs" style="left:549px;top:17px;width:52px;height:13px;background:var(--brand-blue);color:#fff;font-size:7px;text-align:center;line-height:13px">Verify</div>
  </div>

  <div class="select plain" style="left:199px;top:200px;width:181px">Search by name or nickname</div>
  <div class="select" style="left:388px;top:200px;width:94px">Department</div>
  <div class="select" style="left:491px;top:200px;width:94px">Branch</div>
  <div class="select" style="left:594px;top:200px;width:94px">Position</div>
  <div class="select" style="left:698px;top:200px;width:97px">Subsidiary</div>

  <div class="ptable">
    <div class="prow head"><div>EMPLOYEE<br>NAME</div><div>WAGES</div><div>OTHER<br>PAYMENTS</div><div>CONTRIBUTIONS</div><div>TAX</div><div>EXPENSES</div><div>NETT<br>PAYABLE</div><div>PAYMENT<br>METHOD</div><div>STATUS</div></div>
    <div class="prow"><div class="nm">, asdf<b>Logistic Officer</b></div><div class="or">25,000,000.00</div><div class="bl">-12,113,709.68</div><div class="rd">-1,409,397.00</div><div class="rd">-1,409,397.00</div><div class="bl">0.00</div><div class="bl">0.00</div><div><i class="cash"></i></div><div><span class="status">Pending</span> ⌃⌄</div></div>
    <div class="prow"><div class="nm">100, Employee<b>HR Administrator</b></div><div class="or">25,000,000.00</div><div class="bl">0.00</div><div class="rd">-1,409,397.00</div><div class="rd">-1,409,397.00</div><div class="bl">0.00</div><div class="bl">0.00</div><div style="color:var(--green)">⬇</div><div><span class="status ok">Verified</span> ⌃⌄</div></div>
    <div class="prow"><div class="nm">11, Employee<b>CFO</b></div><div class="or">25,000,000.00</div><div class="bl">0.00</div><div class="rd">-1,409,397.00</div><div class="rd">-1,409,397.00</div><div class="bl">0.00</div><div class="bl">0.00</div><div><i class="cash"></i></div><div><span class="status">Pending</span> ⌃⌄</div></div>
    <div class="prow"><div class="nm">12, Employee<b>Factory Worker</b></div><div class="or">25,000,000.00</div><div class="bl">0.00</div><div class="rd">-1,409,397.00</div><div class="rd">-1,409,397.00</div><div class="bl">0.00</div><div class="bl">0.00</div><div><i class="cash"></i></div><div><span class="status">Pending</span> ⌃⌄</div></div>
    <div class="prow"><div class="nm">13, Employee<b>Logistic Officer</b></div><div class="or">25,000,000.00</div><div class="bl">0.00</div><div class="rd">-1,409,397.00</div><div class="rd">-1,409,397.00</div><div class="bl">0.00</div><div class="bl">0.00</div><div><i class="cash"></i></div><div><span class="status">Pending</span> ⌃⌄</div></div>
    <div class="prow"><div class="nm">14, Employee<b>Factory Worker</b></div><div class="or">25,000,000.00</div><div class="bl">0.00</div><div class="rd">-1,409,397.00</div><div class="rd">-1,409,397.00</div><div class="bl">0.00</div><div class="bl">0.00</div><div><i class="cash"></i></div><div><span class="status">Pending</span> ⌃⌄</div></div>
    <div class="prow"><div class="nm">15, Employee<b>QA Manager</b></div><div class="or">25,000,000.00</div><div class="bl">2,400,000.00</div><div class="rd">-1,409,397.00</div><div class="rd">-1,409,397.00</div><div class="bl">0.00</div><div class="bl">0.00</div><div><i class="cash"></i></div><div><span class="status">Pending</span> ⌃⌄</div></div>
    <div class="prow"><div class="nm">16, Employee<b>Factory Worker</b></div><div class="or">25,000,000.00</div><div class="bl">200,000.00</div><div class="rd">-1,409,397.00</div><div class="rd">-1,409,397.00</div><div class="bl">0.00</div><div class="bl">0.00</div><div><i class="cash"></i></div><div><span class="status">Pending</span> ⌃⌄</div></div>
    <div class="prow"><div class="nm">16, Employee<b>Factory Worker</b></div><div class="or">25,000,000.00</div><div class="bl">1,500,000.00</div><div class="rd">-1,409,397.00</div><div class="rd">-1,409,397.00</div><div class="bl">0.00</div><div class="bl">0.00</div><div><i class="cash"></i></div><div><span class="status">Pending</span> ⌃⌄</div></div>
    <div class="prow"><div class="nm">13, Employee<b>Logistic Officer</b></div><div class="or">25,000,000.00</div><div class="bl">0.00</div><div class="rd">-1,409,397.00</div><div class="rd">-1,409,397.00</div><div class="bl">0.00</div><div class="bl">0.00</div><div><i class="cash"></i></div><div><span class="status">Pending</span> ⌃⌄</div></div>
    <div class="prow"><div class="nm">14, Employee<b>Factory Worker</b></div><div class="or">25,000,000.00</div><div class="bl">0.00</div><div class="rd">-1,409,397.00</div><div class="rd">-1,409,397.00</div><div class="bl">0.00</div><div class="bl">0.00</div><div><i class="cash"></i></div><div><span class="status">Pending</span> ⌃⌄</div></div>
    <div class="prow"><div class="nm">15, Employee<b>QA Manager</b></div><div class="or">25,000,000.00</div><div class="bl">1,200,000.00</div><div class="rd">-1,409,397.00</div><div class="rd">-1,409,397.00</div><div class="bl">0.00</div><div class="bl">0.00</div><div><i class="cash"></i></div><div><span class="status">Pending</span> ⌃⌄</div></div>
    <div class="prow"><div class="nm">16, Employee<b>Factory Worker</b></div><div class="or">25,000,000.00</div><div class="bl">0.00</div><div class="rd">-1,409,397.00</div><div class="rd">-1,409,397.00</div><div class="bl">0.00</div><div class="bl">0.00</div><div><i class="cash"></i></div><div><span class="status">Pending</span> ⌃⌄</div></div>
    <div class="prow"><div class="nm">16, Employee<b>Factory Worker</b></div><div class="or">25,000,000.00</div><div class="bl">0.00</div><div class="rd">-1,409,397.00</div><div class="rd">-1,409,397.00</div><div class="bl">0.00</div><div class="bl">0.00</div><div><i class="cash"></i></div><div><span class="status">Pending</span> ⌃⌄</div></div>
    <div class="prow"><div class="nm">15, Employee<b>QA Manager</b></div><div class="or">25,000,000.00</div><div class="bl">0.00</div><div class="rd">-1,409,397.00</div><div class="rd">-1,409,397.00</div><div class="bl">0.00</div><div class="bl">0.00</div><div><i class="cash"></i></div><div><span class="status">Pending</span> ⌃⌄</div></div>
    <div class="prow"><div class="nm">16, Employee<b>Factory Worker</b></div><div class="or">25,000,000.00</div><div class="bl">0.00</div><div class="rd">-1,409,397.00</div><div class="rd">-1,409,397.00</div><div class="bl">0.00</div><div class="bl">0.00</div><div><i class="cash"></i></div><div><span class="status">Pending</span> ⌃⌄</div></div>
    <div class="prow"><div class="nm">16, Employee<b>Factory Worker</b></div><div class="or">25,000,000.00</div><div class="bl">0.00</div><div class="rd">-1,409,397.00</div><div class="rd">-1,409,397.00</div><div class="bl">0.00</div><div class="bl">0.00</div><div><i class="cash"></i></div><div><span class="status">Pending</span> ⌃⌄</div></div>
  </div>
  <div class="pager"><span class="dark">‹‹</span><span class="on">1</span><span>2</span><span>3</span><span>4</span><span>5</span><span class="dark">››</span></div>
</section>

<!-- WEEKLY CALENDAR -->
<section class="screen" style="left:47px;top:659px;height:585px">
  <aside class="sidebar">
    <div class="brand"><span class="brand-dot"></span><span class="brand-name">QuillStaff</span></div>
    <div class="nav-item"><i class="nav-icon"></i>DASHBOARD</div>
    <div class="nav-item"><i class="nav-icon"></i>EMPLOYEES</div>
    <div class="nav-item active"><i class="nav-icon"></i>CALENDAR</div>
    <div class="nav-item"><i class="nav-icon"></i>EXPENSES</div>
    <div class="nav-item"><i class="nav-icon"></i>PAYROLL</div>
    <div class="nav-item"><i class="nav-icon"></i>LOANS</div>
    <div class="nav-item"><i class="nav-icon"></i>PERFORMANCE</div>
    <div class="nav-item"><i class="nav-icon"></i>ENGAGEMENT</div>
    <div class="nav-item"><i class="nav-icon"></i>REPORTS</div>
    <div class="nav-item"><i class="nav-icon"></i>SETTINGS</div>
    <div class="powered">Powered by: <b>QuillStaff</b></div>
    <div class="legal">Terms | Privacy</div>
  </aside>
  <header class="topbar">
    <span class="lang">English ⌄</span><span class="help"></span>
    <div class="user"><span class="avatar" role="img" aria-label="Admin profile photo"></span><strong>Admin, Demo</strong><small>HR Administrator ⌄</small></div>
  </header>

  <div class="tabs">
    <span style="left:199px;top:76px">DAILY</span>
    <span style="left:249px;top:76px;color:var(--link-blue);border-bottom:2px solid var(--link-blue);padding:0 9px 6px">WEEKLY</span>
    <span style="left:311px;top:76px">MONTHLY</span>
    <span style="left:380px;top:76px">LIST</span>
    <span style="left:423px;top:76px">GEO-TAGGING</span>
    <span style="left:596px;top:76px">SELECT TIMEZONE</span>
  </div>
  <div class="select" style="left:674px;top:70px;width:121px">Current Time Zone</div>

  <div class="tile t1" style="left:199px;top:105px"><svg width="20" height="17" viewBox="0 0 20 17" fill="none" stroke="#fff" stroke-width="1.3"><rect x="1" y="2" width="18" height="14"/><path d="M1 6h18M5 0v4M15 0v4"/></svg><span class="num">12</span><span class="lbl">EVENT AMENDMENTS</span></div>
  <div class="tile t2" style="left:352px;top:105px"><svg width="18" height="18" viewBox="0 0 18 18" fill="none" stroke="#fff" stroke-width="1.3"><rect x="2" y="1" width="13" height="16"/><path d="M5 5h7M5 9h7M5 13h5"/></svg><span class="num">2</span><span class="lbl">LEAVE REQUESTS</span></div>
  <div class="tile t3" style="left:505px;top:105px"><svg width="20" height="18" viewBox="0 0 20 18" fill="none" stroke="#fff" stroke-width="1.3"><rect x="1" y="3" width="14" height="14"/><circle cx="14" cy="7" r="5"/></svg><span class="num">7</span><span class="lbl">EVENT REQUESTS</span></div>
  <div class="tile t4" style="left:658px;top:105px"><svg width="20" height="18" viewBox="0 0 20 18" fill="none" stroke="#fff" stroke-width="1.3"><rect x="1" y="1" width="14" height="16"/><circle cx="15" cy="13" r="4"/></svg><span class="num">1</span><span class="lbl">PAYROLLS PENDING</span></div>

  <div class="select plain" style="left:199px;top:168px;width:122px">Search by name or nickname</div>
  <div class="select" style="left:328px;top:168px;width:67px">Department</div>
  <div class="select" style="left:403px;top:168px;width:58px">Branch</div>
  <div class="select" style="left:467px;top:168px;width:61px">Group</div>
  <div class="select" style="left:535px;top:168px;width:57px">Activity</div>
  <div class="select" style="left:600px;top:168px;width:61px">Activity Type</div>
  <div class="select" style="left:667px;top:168px;width:54px">Position</div>
  <div class="select" style="left:728px;top:168px;width:67px">First Name</div>

  <div class="abs" style="left:180px;right:0;top:203px;height:380px;background:#fff"></div>
  <div class="abs" style="left:180px;right:0;top:203px;height:60px;background:var(--page)"></div>
  <div class="abs" style="left:199px;top:232px;font-size:9px;color:var(--link-blue);font-weight:700">‹ &nbsp; Week 5 of May 2020 &nbsp; ›</div>
  <div class="dayhead" style="left:361px">MON<br><small>25/5/20</small></div>
  <div class="dayhead" style="left:424px">TUE<br><small>26/5/20</small></div>
  <div class="dayhead" style="left:487px">WED<br><small>27/5/20</small></div>
  <div class="dayhead" style="left:550px">THU<br><small>28/5/20</small></div>
  <div class="dayhead" style="left:613px">FRI<br><small>29/5/20</small></div>
  <div class="dayhead" style="left:676px">SAT<br><small>30/5/20</small></div>
  <div class="dayhead" style="left:739px">SUN<br><small>31/5/20</small></div>
  <div class="abs" style="left:323px;top:250px;font-size:6.5px;font-weight:700;color:var(--teal)">ON DUTY</div>
  <div class="abs" style="left:361px;top:250px;width:437px;display:flex;font-size:6.5px;font-weight:700;color:var(--teal)"><span style="width:63px;text-align:center">140</span><span style="width:63px;text-align:center">140</span><span style="width:63px;text-align:center">113</span><span style="width:63px;text-align:center">134</span><span style="width:63px;text-align:center">160</span><span style="width:63px;text-align:center">52</span></div>
  <div class="abs" style="left:320px;top:263px;width:40px;height:19px;background:#222;color:#fff;font-size:6.5px;font-weight:700;text-align:center;line-height:19px">HOURS</div>
  <div class="abs" style="left:320px;top:282px;width:1px;height:303px;background:#ddd"></div>

  <div class="abs" style="left:180px;top:282px;width:657px">
    <div class="emp" style="top:0;left:0"><span class="avatar" role="img" aria-label="Employee photo"></span><span class="nm">108, Employee</span><span class="sub">Branch B | Department 6</span><span class="hrs">40</span></div>
    <div class="emp" style="top:30px;left:0"><span class="avatar" role="img" aria-label="Employee photo"></span><span class="nm">108, Employee</span><span class="sub">Branch B | Department 6</span><span class="hrs">30</span></div>
    <div class="emp" style="top:60px;left:0"><span class="avatar" role="img" aria-label="Employee photo"></span><span class="nm">108, Employee</span><span class="sub">Branch B | Department 6</span><span class="hrs">0</span></div>
    <div class="emp" style="top:90px;left:0"><span class="avatar" role="img" aria-label="Employee photo"></span><span class="nm">108, Employee</span><span class="sub">Branch B | Department 6</span><span class="hrs">0</span></div>
    <div class="emp" style="top:120px;left:0"><span class="avatar" role="img" aria-label="Employee photo"></span><span class="nm">108, Employee</span><span class="sub">Branch B | Department 6</span><span class="hrs">0</span></div>
    <div class="emp" style="top:150px;left:0"><span class="avatar" role="img" aria-label="Employee photo"></span><span class="nm">108, Employee</span><span class="sub">Branch B | Department 6</span><span class="hrs">0</span></div>
    <div class="emp" style="top:180px;left:0"><span class="avatar" role="img" aria-label="Employee photo"></span><span class="nm">108, Employee</span><span class="sub">Branch B | Department 6</span><span class="hrs">0</span></div>
    <div class="emp" style="top:210px;left:0"><span class="avatar" role="img" aria-label="Employee photo"></span><span class="nm">108, Employee</span><span class="sub">Branch B | Department 6</span><span class="hrs">0</span></div>
    <div class="emp" style="top:240px;left:0"><span class="avatar" role="img" aria-label="Employee photo"></span><span class="nm">108, Employee</span><span class="sub">Branch B | Department 6</span><span class="hrs">0</span></div>
    <div class="emp" style="top:270px;left:0"><span class="avatar" role="img" aria-label="Employee photo"></span><span class="nm">108, Employee</span><span class="sub">Branch B | Department 6</span><span class="hrs">0</span></div>
  </div>

  <div class="shift wd" style="left:366px;top:291px">10:00-19:00</div>
  <div class="shift wd" style="left:429px;top:291px">10:00-19:00</div>
  <div class="shift wd" style="left:492px;top:291px">10:00-19:00</div>
  <div class="shift wd" style="left:555px;top:291px">10:00-19:00</div>
  <div class="shift wd" style="left:618px;top:291px">10:00-19:00</div>
  <div class="shift we" style="left:681px;top:291px">10:00-19:00</div>
  <div class="shift we" style="left:744px;top:291px">10:00-19:00</div>
  <div class="shift wd" style="left:366px;top:321px">10:00-19:00</div>
  <div class="shift wd" style="left:429px;top:321px">10:00-19:00</div>
  <div class="shift wd" style="left:492px;top:321px">10:00-19:00</div>
  <div class="shift wd" style="left:555px;top:321px">10:00-19:00</div>
  <div class="shift wd" style="left:618px;top:321px">10:00-19:00</div>
  <div class="shift we" style="left:681px;top:321px">10:00-19:00</div>
  <div class="shift we" style="left:744px;top:321px">10:00-19:00</div>
  <div class="abs" style="left:803px;top:285px;width:3px;height:22px;background:#222"></div>
</section>

<!-- EMPLOYEE LEAVE PROFILE -->
<section class="screen" style="left:578px;top:659px;height:836px;background:#777">
  <aside class="sidebar" style="background:#161616"></aside>
  <div class="modal">
    <div class="mhead">
      <span class="avatar abs" role="img" aria-label="Employee profile photo" style="left:10px;top:14px;width:40px;height:40px"></span>
      <div class="abs" style="left:57px;top:16px;font-size:17px">103 Employee</div>
      <div class="abs" style="left:57px;top:40px;font-size:7.5px">Postion 18|Department 6|Branch B</div>
      <div class="abs" style="left:664px;top:22px;font-size:7.5px">✉ &nbsp;rina@quillstaff.example</div>
      <div class="abs" style="left:760px;top:22px;font-size:7.5px">IDCA00107</div>
      <div class="abs" style="left:664px;top:42px;font-size:7.5px">✆ &nbsp;N/A</div>
      <div class="abs" style="left:748px;top:42px;font-size:7.5px">● &nbsp;1700</div>
    </div>
    <div class="mtabs">
      <span style="left:10px">EMPLOYEE PROFILE</span>
      <span style="left:114px">EMPLOYMENT INFO</span>
      <span style="left:219px">SCHEDULE</span>
      <span style="left:277px;color:var(--link-blue);border-bottom:2px solid var(--link-blue);padding:0 12px 6px">LEAVE</span>
      <span style="left:357px">PAYSLIP</span>
      <span style="left:754px">ACTIVE <i style="display:inline-block;width:12px;height:7px;border-radius:4px;background:var(--teal);margin-left:6px;vertical-align:middle"></i></span>
    </div>
    <div class="abs" style="left:0;right:0;top:102px;height:1px;background:var(--rule)"></div>

    <div class="abs" style="left:9px;top:113px;width:793px;height:237px;border:1px solid var(--rule)">
      <div class="abs" style="left:8px;top:6px;width:112px;height:21px;background:var(--teal-light);color:#fff;font-size:8px;line-height:21px;padding-left:26px">LEAVE REQUESTS</div>
      <div class="abs" style="left:368px;top:12px;font-size:8px">‹ &nbsp;&nbsp; 2020 &nbsp;&nbsp; ›</div>
      <svg class="abs" style="left:0;top:33px" width="792" height="203" viewBox="0 0 792 203" font-family="Lato,sans-serif" font-size="6.5" text-anchor="middle">
        <rect x="0" y="0" width="40" height="203" fill="#1f4f93"/>
        <rect x="40" y="0" width="752" height="18" fill="#fff"/>
        <g fill="#222">
          <text x="52" y="12">1</text><text x="76" y="12">2</text><text x="101" y="12">3</text><text x="125" y="12">4</text><text x="149" y="12">5</text><text x="173" y="12">6</text><text x="198" y="12">7</text><text x="222" y="12">8</text><text x="246" y="12">9</text><text x="270" y="12">10</text><text x="295" y="12">11</text><text x="319" y="12">12</text><text x="343" y="12">13</text><text x="367" y="12">14</text><text x="392" y="12">15</text><text x="416" y="12">16</text><text x="440" y="12">17</text><text x="465" y="12">18</text><text x="489" y="12">19</text><text x="513" y="12">20</text><text x="537" y="12">21</text><text x="562" y="12">22</text><text x="586" y="12">23</text><text x="610" y="12">24</text><text x="634" y="12">25</text><text x="659" y="12">26</text><text x="683" y="12">27</text><text x="707" y="12">28</text><text x="731" y="12">29</text><text x="756" y="12">30</text><text x="780" y="12">31</text>
        </g>
        <g>
          <rect x="40" y="18" width="752" height="15" fill="var(--grid-a)"/><rect x="40" y="33" width="752" height="15" fill="var(--grid-b)"/>
          <rect x="40" y="48" width="752" height="15" fill="var(--grid-a)"/><rect x="40" y="63" width="752" height="15" fill="var(--grid-b)"/>
          <rect x="40" y="78" width="752" height="15" fill="var(--grid-a)"/><rect x="40" y="93" width="752" height="15" fill="var(--grid-b)"/>
          <rect x="40" y="108" width="752" height="15" fill="var(--grid-a)"/><rect x="40" y="123" width="752" height="15" fill="var(--grid-b)"/>
          <rect x="40" y="138" width="752" height="15" fill="var(--grid-a)"/><rect x="40" y="153" width="752" height="15" fill="var(--grid-b)"/>
          <rect x="40" y="168" width="752" height="15" fill="var(--grid-a)"/><rect x="40" y="183" width="752" height="20" fill="var(--grid-b)"/>
        </g>
        <g fill="var(--grid-block)">
          <rect x="105" y="19" width="36" height="13"/><rect x="235" y="19" width="36" height="13"/><rect x="435" y="19" width="36" height="13"/><rect x="610" y="19" width="36" height="13"/>
          <rect x="45" y="34" width="15" height="13"/><rect x="180" y="34" width="36" height="13"/><rect x="305" y="34" width="36" height="13"/><rect x="510" y="34" width="36" height="13"/><rect x="670" y="34" width="24" height="13"/>
          <rect x="45" y="49" width="15" height="13"/><rect x="165" y="49" width="36" height="13"/><rect x="290" y="49" width="36" height="13"/><rect x="495" y="49" width="36" height="13"/><rect x="660" y="49" width="36" height="13"/>
          <rect x="105" y="64" width="36" height="13"/><rect x="235" y="64" width="36" height="13"/><rect x="435" y="64" width="36" height="13"/><rect x="610" y="64" width="36" height="13"/>
          <rect x="45" y="79" width="15" height="13"/><rect x="105" y="79" width="36" height="13"/><rect x="180" y="79" width="36" height="13"/><rect x="305" y="79" width="36" height="13"/>
          <rect x="45" y="94" width="15" height="13"/><rect x="165" y="94" width="36" height="13"/><rect x="290" y="94" width="36" height="13"/><rect x="495" y="94" width="36" height="13"/><rect x="660" y="94" width="36" height="13"/>
          <rect x="385" y="109" width="36" height="13"/>
          <rect x="180" y="124" width="36" height="13"/><rect x="305" y="124" width="36" height="13"/>
          <rect x="165" y="139" width="36" height="13"/><rect x="290" y="139" width="36" height="13"/><rect x="525" y="139" width="36" height="13"/>
          <rect x="75" y="154" width="36" height="13"/><rect x="140" y="154" width="36" height="13"/><rect x="215" y="154" width="36" height="13"/><rect x="335" y="154" width="36" height="13"/><rect x="590" y="154" width="36" height="13"/>
          <rect x="45" y="169" width="15" height="13"/><rect x="165" y="169" width="36" height="13"/><rect x="290" y="169" width="36" height="13"/><rect x="495" y="169" width="36" height="13"/><rect x="660" y="169" width="36" height="13"/>
          <rect x="75" y="184" width="36" height="13"/><rect x="215" y="184" width="36" height="13"/><rect x="335" y="184" width="36" height="13"/>
        </g>
        <g fill="var(--orange)">
          <rect x="45" y="19" width="20" height="13"/><rect x="45" y="64" width="20" height="13"/>
          <rect x="768" y="49" width="24" height="13"/><rect x="768" y="94" width="24" height="13"/>
          <rect x="510" y="79" width="186" height="13"/>
        </g>
        <g fill="#fff" font-size="6.5" font-weight="700">
          <text x="20" y="28">JAN</text><text x="20" y="43">FEB</text><text x="20" y="58">MAR</text><text x="20" y="73">APR</text><text x="20" y="88">MAY</text><text x="20" y="103">JUN</text><text x="20" y="118">JUL</text><text x="20" y="133">AUG</text><text x="20" y="148">SEP</text><text x="20" y="163">OCT</text><text x="20" y="178">NOV</text><text x="20" y="195">DEC</text>
        </g>
      </svg>
    </div>

    <h2 class="h" style="left:9px;top:370px">LEAVE OVERVIEW</h2>
    <h2 class="h" style="left:404px;top:370px">PENDING LEAVE OVERVIEW</h2>

    <div class="card" style="left:9px;top:392px;width:378px;height:168px">
      <div class="abs" style="left:0;right:0;top:0;height:27px;background:#f3f3f3;font-size:6.5px;font-weight:700">
        <span class="abs" style="left:9px;top:10px">LEAVE TYPE</span><span class="abs" style="left:92px;top:10px">AWARDED</span><span class="abs" style="left:172px;top:10px">PENDING</span><span class="abs" style="left:250px;top:10px">TAKEN</span><span class="abs" style="left:315px;top:10px">BALANCE</span>
      </div>
      <div class="abs" style="left:0;right:0;top:27px;height:32px;border-bottom:1px solid var(--rule);font-size:7.5px">
        <span class="pill bg-orange abs" style="left:9px;top:11px;width:68px;text-align:center">Annual Leave</span><span class="abs" style="left:92px;top:14px">5.00</span><span class="abs" style="left:172px;top:14px">0.00</span><span class="abs" style="left:250px;top:14px">0.00</span><span class="abs bl" style="left:315px;top:14px">5.00</span>
      </div>
      <div class="abs" style="left:0;right:0;top:59px;height:32px;border-bottom:1px solid var(--rule);font-size:7.5px">
        <span class="pill bg-red abs" style="left:9px;top:11px;width:68px;text-align:center">Sick Leave</span><span class="abs" style="left:172px;top:14px">2.00</span><span class="abs" style="left:250px;top:14px">2.00</span>
      </div>
      <span class="pill bg-blue abs" style="left:9px;top:146px">Adjust Balance</span>
    </div>

    <div class="card" style="left:404px;top:392px;width:380px;height:173px">
      <div class="abs" style="left:0;right:0;top:0;height:58px;border-bottom:1px solid var(--rule);font-size:7.5px">
        <span class="pill bg-orange abs" style="left:11px;top:9px;width:72px;text-align:center">Annual Leave</span><span class="abs" style="left:95px;top:12px">( 1.00 Days )</span><span class="abs" style="left:11px;top:37px">10Jun 2020 &nbsp;- &nbsp;10Jun 2020</span>
        <span class="xbtn" style="left:335px;top:13px">X</span><span class="abs" style="left:324px;top:40px;font-size:6px;font-weight:700;color:var(--link-blue)">SHOW MORE</span>
      </div>
      <div class="abs" style="left:0;right:0;top:58px;height:56px;border-bottom:1px solid var(--rule);font-size:7.5px">
        <span class="pill bg-red abs" style="left:11px;top:11px;width:72px;text-align:center">Sick Leave</span><span class="abs" style="left:95px;top:14px">( 1.00 Days )</span><span class="abs" style="left:11px;top:37px">10Jun 2020 &nbsp;- &nbsp;10Jun 2020</span>
        <span class="xbtn" style="left:335px;top:7px">X</span><span class="abs" style="left:324px;top:34px;font-size:6px;font-weight:700;color:var(--link-blue)">SHOW MORE</span>
      </div>
      <div class="abs" style="left:0;right:0;top:114px;height:56px;font-size:7.5px">
        <span class="pill bg-red abs" style="left:11px;top:8px;width:72px;text-align:center">Sick Leave</span><span class="abs" style="left:95px;top:11px">( 1.00 Days )</span><span class="abs" style="left:11px;top:36px">10Jun 2020 &nbsp;- &nbsp;10Jun 2020</span>
        <span class="xbtn" style="left:335px;top:9px">X</span><span class="abs" style="left:324px;top:36px;font-size:6px;font-weight:700;color:var(--link-blue)">SHOW MORE</span>
      </div>
    </div>

    <h2 class="h" style="left:9px;top:585px">LEAVE HISTORY</h2>
    <div class="card" style="left:9px;top:607px;width:775px;height:193px">
      <div class="abs" style="left:0;right:0;top:0;height:33px;background:#f3f3f3;font-size:6.5px;font-weight:700">
        <span class="abs" style="left:16px;top:13px">DATE</span><span class="abs" style="left:148px;top:13px">DAYS</span><span class="abs" style="left:262px;top:13px">TYPE</span><span class="abs" style="left:376px;top:13px">DESCRIPTION</span><span class="abs" style="left:566px;top:13px">NOTES</span><span class="abs" style="left:685px;top:13px">STATUS</span>
      </div>
      <div class="hist-row" style="top:33px"><span style="left:16px">20 MAY 2020 &nbsp;- &nbsp;31 MAY 2020</span><span style="left:142px">3.00</span><span class="pill bg-orange" style="left:261px;top:10px;width:69px;text-align:center;position:absolute">Annual Leave</span><span style="left:376px">Duis consectetur bibendum</span><span style="left:566px">Auto Approved</span><span style="left:685px;color:var(--green);font-size:7px">Approved</span></div>
      <div class="hist-row" style="top:67px"><span style="left:16px">20 MAY 2020 &nbsp;- &nbsp;31 MAY 2020</span><span style="left:142px">3.00</span><span class="pill bg-orange" style="left:261px;top:10px;width:69px;text-align:center;position:absolute">Annual Leave</span><span style="left:376px">Duis consectetur bibendum</span><span style="left:566px">Auto Approved</span><span style="left:685px;color:var(--green);font-size:7px">Approved</span></div>
      <div class="hist-row" style="top:101px"><span style="left:16px">20 MAY 2020 &nbsp;- &nbsp;31 MAY 2020</span><span style="left:142px">3.00</span><span class="pill bg-orange" style="left:261px;top:10px;width:69px;text-align:center;position:absolute">Annual Leave</span><span style="left:376px">Duis consectetur bibendum</span><span style="left:566px">Auto Approved</span><span style="left:685px;color:var(--green);font-size:7px">Approved</span></div>
      <div class="hist-row" style="top:135px;border:0"><span style="left:16px">20 MAY 2020 &nbsp;- &nbsp;31 MAY 2020</span><span style="left:142px">3.00</span><span class="pill bg-orange" style="left:261px;top:10px;width:69px;text-align:center;position:absolute">Annual Leave</span><span style="left:376px">Duis consectetur bibendum</span><span style="left:566px">Auto Approved</span><span style="left:685px;color:var(--green);font-size:7px">Approved</span></div>
    </div>
  </div>
</section>

</body>
</html>
```